Pagecraft 6 pages GLAM design for hair salon

Hi guys.
I need a glam & easy to navigate web design for my (women only) new hair salon.
I have a logo. You can see in attached files.
I like 3d backgrounds.
My favourite colours choice: any variety of pink(hot & very soft), white, black, grey.
I would like to see website very feminine, glamorous & kind of old Hollywood and Dorinda Kessaly inspired.
Of course it should have plug ins, like social media, map, security etc.
My website now: http://velmorinstyling.example

Designs what I like:
http://trulanbeauty.example
http://pevrilglowlounge.example
http://www.quintarvisualworks.example/boutique-graphic-web-folio.html

Target Market(s)

WOMEN

Industry/Entity Type

Boutique

Requirements
Should not have
• any cartoon or other characters!

```html
<!DOCTYPE html>
<html lang="en">
<head>
<meta charset="utf-8">
<title>Velmorin Styling</title>
<link href="https://fonts.googleapis.com/css2?family=Gelasio:ital,wght@0,400;1,400&family=Lobster&family=Open+Sans&display=swap" rel="stylesheet">
<style>
  :root {
    --pink: #c94b82;
    --pink-deep: #b83a72;
    --pink-soft: #f7dbe7;
    --pink-pale: #fdf2f6;
    --grey: #6d6d6d;
    --grey-dark: #3f3f3f;
    --white: #ffffff;
  }
  * { margin: 0; padding: 0; box-sizing: border-box; }
  html, body { width: 1200px; height: 1200px; overflow: hidden; }
  body {
    position: relative;
    font-family: "Gelasio", Georgia, serif;
    background: radial-gradient(circle at 20% 15%, #f9dde8 0, transparent 260px),
                radial-gradient(circle at 85% 20%, #f9dde8 0, transparent 240px),
                radial-gradient(circle at 10% 85%, #f9dde8 0, transparent 220px),
                radial-gradient(circle at 90% 88%, #f9dde8 0, transparent 240px),
                var(--pink-pale);
  }
  .site-brand {
    position: absolute; left: 400px; top: 30px; width: 400px; height: 190px;
    display: flex; align-items: center; justify-content: center; gap: 12px;
  }
  .site-brand__mark { width: 14px; height: 14px; border-radius: 50%; background: var(--pink); }
  .site-brand__name {
    font-family: "Gelasio", Georgia, serif; font-size: 30px;
    color: var(--pink-deep); white-space: nowrap;
  }
  .main-nav { position: absolute; left: 250px; top: 235px; display: flex; height: 50px; }
  .main-nav a {
    font-family: "Lobster", cursive; font-size: 19px; color: var(--pink);
    text-decoration: none; display: flex; align-items: center; height: 50px;
  }
  .main-nav .is-active {
    background: linear-gradient(#e583ad, var(--pink)); color: var(--white);
    width: 79px; justify-content: center; border-radius: 3px 3px 0 0;
  }
  .wave { position: absolute; left: 0; width: 1200px; height: 6px; }
  .hero-band { position: absolute; left: 0; top: 289px; width: 1200px; height: 297px; background: rgba(255,255,255,.55); }
  .hero-photo {
    position: absolute; left: 110px; top: 289px; width: 527px; height: 297px;
    background: linear-gradient(90deg, #f1d3c4 0%, #7a3a22 45%, #9a4a2a 70%, #f6ece8 100%);
  }
  .hero-quote {
    position: absolute; left: 671px; top: 362px; width: 400px;
    font-style: italic; color: var(--pink); font-size: 19px; line-height: 1.25;
  }
  .hero-quote b { font-weight: 400; font-size: 30px; }
  .slider-dots { position: absolute; left: 853px; top: 539px; display: flex; gap: 9px; }
  .slider-dots span {
    width: 24px; height: 22px; border-radius: 3px; background: var(--pink);
    color: var(--white); font-size: 11px; font-style: italic;
    display: flex; align-items: center; justify-content: center;
  }
  .welcome { position: absolute; left: 14px; top: 614px; width: 1200px; text-align: center; font-style: italic; }
  .welcome h1 { font-weight: 400; font-size: 25px; color: var(--pink); margin-bottom: 8px; }
  .welcome p { font-size: 15.5px; color: var(--grey-dark); line-height: 1.3; width: 840px; margin: 0 auto 17px; }
  .more-link { color: var(--pink); font-size: 16px; font-style: italic; text-decoration: none; }
  .welcome .more-link { display: inline-block; margin-top: -4px; }
  .recent-title { position: absolute; left: 127px; top: 785px; font-weight: 400; font-style: italic; font-size: 25px; color: var(--pink); }
  .post { position: absolute; top: 832px; width: 302px; }
  .post__photo { height: 128px; border: 1px solid #e07fa8; }
  .post__date { margin-top: 16px; font-style: italic; font-size: 18px; color: var(--grey); letter-spacing: .5px; }
  .post__excerpt { margin-top: 13px; width: 280px; font-style: italic; font-size: 13.5px; color: var(--grey); line-height: 1.3; }
  .post .more-link { display: block; text-align: right; margin-top: 4px; }
  .calendar-tab {
    position: absolute; left: 1164px; top: 634px; width: 36px; height: 97px;
    background: var(--pink); border-radius: 4px 0 0 4px; color: var(--white);
    font-style: italic; font-size: 15px; writing-mode: vertical-rl; transform: rotate(180deg);
    display: flex; align-items: center; justify-content: center;
  }
  .social { position: absolute; left: 540px; top: 1108px; display: flex; gap: 5px; }
  .social span { width: 26px; height: 27px; border-radius: 4px; background: var(--pink); }
  .social span:nth-child(1) { background: #4a6ea9; }
  .social span:nth-child(2) { background: #4fb4d8; }
  .social span:nth-child(3) { background: #9a9a9a; }
  .social span:nth-child(4) { background: #d2343e; }
  .copyright { position: absolute; left: 0; top: 1157px; width: 1200px; text-align: center; font-family: "Open Sans", Arial, sans-serif; font-size: 12px; color: var(--grey-dark); }
</style>
</head>
<body>
  <svg width="0" height="0" style="position:absolute">
    <defs>
      <pattern id="zigzag" width="8" height="6" patternUnits="userSpaceOnUse">
        <path d="M0 1 L4 5 L8 1" fill="none" stroke="#c94b82" stroke-width="2"/>
      </pattern>
    </defs>
  </svg>

  <header class="site-brand">
    <span class="site-brand__mark"></span>
    <span class="site-brand__name">Velmorin Styling</span>
  </header>

  <nav class="main-nav">
    <a class="is-active" href="#">Home</a>
    <a href="#" style="margin-left:43px">About Us</a>
    <a href="#" style="margin-left:63px">Services</a>
    <a href="#" style="margin-left:63px">Gallery</a>
    <a href="#" style="margin-left:62px">Blog</a>
    <a href="#" style="margin-left:63px">Contact Us</a>
  </nav>

  <svg class="wave" style="top:283px"><rect width="1200" height="6" fill="url(#zigzag)"/></svg>

  <div class="hero-band"></div>
  <div class="hero-photo" role="img" aria-label="Woman with long curly auburn hair decorated with yellow petals"></div>
  <p class="hero-quote">Our salon is <b>based on the belief</b><br><b>that our customers' needs</b> are<br>of the utmost <b>importance.</b></p>
  <div class="slider-dots"><span>1</span><span>2</span><span>3</span></div>

  <svg class="wave" style="top:585px"><rect width="1200" height="6" fill="url(#zigzag)"/></svg>

  <section class="welcome">
    <h1>Welcome To Our Website!</h1>
    <p>Our salon is based on the belief that our customers' needs are of the utmost importance. Our team is committed to meeting those needs. As a result, a high percentage of our business is from repeat customers and referrals.</p>
    <p>We would welcome the opportunity to earn your trust and deliver you the best service in the industry!</p>
    <a class="more-link" href="#">about more</a>
  </section>

  <h2 class="recent-title">Recent Post</h2>

  <article class="post" style="left:127px">
    <div class="post__photo" role="img" aria-label="Elegant curled updo hairstyle" style="background:linear-gradient(90deg,#d9c7b8,#5a3424 50%,#efe3da)"></div>
    <p class="post__date">JANUARY 6, 2014</p>
    <p class="post__excerpt">by Dr.M There is too much hairspray on the shelf if you go to the...</p>
    <a class="more-link" href="#" style="margin-right:18px">about more</a>
  </article>
  <article class="post" style="left:440px">
    <div class="post__photo" role="img" aria-label="Woman with dark tousled hair" style="background:linear-gradient(90deg,#2a1c16,#5a3b2c 50%,#1e1612)"></div>
    <p class="post__date">JANUARY 6, 2014</p>
    <p class="post__excerpt">by Dr.M There is too much hairspray on the shelf if you go to the...</p>
    <a class="more-link" href="#" style="margin-right:5px">about more</a>
  </article>
  <article class="post" style="left:754px">
    <div class="post__photo" role="img" aria-label="Blonde bridal updo with hair accessory" style="background:linear-gradient(90deg,#5c4a3c,#d8c4a4 45%,#8a9aa8)"></div>
    <p class="post__date" style="margin-left:8px">JANUARY 6, 2014</p>
    <p class="post__excerpt" style="margin-left:8px">by Dr.M There is too much hairspray on the shelf if you go to the...</p>
    <a class="more-link" href="#" style="margin-right:-6px">about more</a>
  </article>

  <div class="calendar-tab">Calander</div>

  <svg class="wave" style="top:1085px"><rect width="1200" height="6" fill="url(#zigzag)"/></svg>

  <footer>
    <div class="social" aria-label="Social links"><span></span><span></span><span></span><span></span></div>
    <p class="copyright">© 2014.www.velmorinstyling.example</p>
  </footer>
</body>
</html>
```